Thornwell Building Company - advertisement poster

I am looking to print some canvas signs to advertise my general contracting company, Thornwell Building Company. The sign will measure 6' long x 3' high so the size should match that ratio. I already have a logo icon, which is the Letter 'T' and some trees that I would like to incorporate, see attached. I would also like the to have the following information listed:
1) phone number: 472-555-0188
2) email: thornwellbuildingcompany@mailvero.com
3) website: thornwellbuildingcompany.com
4) Lic#4620385
5) I want to use this text: "BUILD WITH THE T-CREW!"

The ad should be relatively simple and clean. Black and Green are my company colors. I am open to creative ideas!

Target Market(s)

People looking to renovate their homes

Industry/Entity Type

Construction

Colors
59FF00
82FF00
B8FF75
E3FFCB
F4FFEA

Requirements
Must have
• Must have my company logo
Should not have
• No photos or complex graphics

```html
<!DOCTYPE html>
<html lang="en">
<head>
<meta charset="utf-8">
<title>Thornwell Building Company – Sign</title>
<link rel="stylesheet" href="https://fonts.googleapis.com/css2?family=Archivo+Black&family=Montserrat:wght@500;600;700&display=swap">
<style>
  :root {
    --green: #6db33f;
    --black: #1c1c1c;
    --white: #ffffff;
    --backdrop: #2e3338;
  }
  * { margin: 0; padding: 0; box-sizing: border-box; }
  html, body { width: 1200px; height: 800px; overflow: hidden; background: var(--backdrop); }
  .canvas { position: relative; width: 1200px; height: 800px; }
  .sign {
    position: absolute; left: 50px; top: 125px; width: 1100px; height: 550px;
    background: var(--green); overflow: hidden;
  }
  .sign-shapes { position: absolute; inset: 0; }
  .headline {
    position: absolute; left: 0; right: 0; top: 70px; text-align: center;
    font-family: "Archivo Black", "Arial Black", sans-serif; color: var(--black);
  }
  .headline-top {
    display: flex; align-items: center; justify-content: center; gap: 22px;
    font-size: 62px; line-height: 1; letter-spacing: 1px;
  }
  .headline-top .rule { display: block; width: 120px; height: 6px; background: var(--black); }
  .headline-main {
    margin-top: 6px; font-size: 140px; line-height: 1; letter-spacing: 22px; padding-left: 22px;
  }
  .brand {
    position: absolute; left: 60px; top: 365px; display: flex; align-items: center; gap: 18px;
    font-family: "Montserrat", sans-serif; font-weight: 700; color: var(--white);
  }
  .brand-mark { width: 54px; height: 54px; background: var(--green); flex: none; }
  .brand-name { font-size: 40px; line-height: 1; letter-spacing: 2px; }
  .brand-sub { display: block; margin-top: 6px; font-size: 15px; letter-spacing: 5.5px; }
  .phone {
    position: absolute; left: 465px; top: 350px; display: flex; align-items: center; gap: 30px;
    font-family: "Montserrat", sans-serif; font-weight: 500; color: var(--white);
    font-size: 76px; line-height: 1; letter-spacing: 1px;
  }
  .contacts {
    position: absolute; left: 470px; top: 442px; display: flex; gap: 34px;
    font-family: "Montserrat", sans-serif; font-weight: 600; color: var(--white); font-size: 17px;
  }
  .contact { display: flex; flex-direction: column; align-items: flex-start; gap: 6px; }
  .contact-line { display: flex; align-items: center; gap: 10px; }
  .contact-tail {
    margin-left: 28px; background: var(--green); color: var(--black);
    font-size: 14px; font-weight: 600; padding: 2px 9px; border-radius: 2px;
  }
  .license {
    position: absolute; left: 60px; top: 518px;
    font-family: "Montserrat", sans-serif; font-weight: 500; font-size: 15px; color: var(--black);
  }
</style>
</head>
<body>
<main class="canvas">
  <section class="sign">
    <svg class="sign-shapes" width="1100" height="550" viewBox="0 0 1100 550" aria-hidden="true">
      <polygon points="0,292 395,292 428,330 1100,330 1100,550 0,550" fill="#1c1c1c"/>
      <polygon points="0,508 290,508 322,550 0,550" fill="#6db33f"/>
    </svg>

    <h1 class="headline">
      <span class="headline-top"><span class="rule"></span>BUILD WITH THE<span class="rule"></span></span>
      <span class="headline-main" style="display:block">T-CREW!</span>
    </h1>

    <div class="brand">
      <span class="brand-mark"></span>
      <div class="brand-name">THORNWELL<span class="brand-sub">BUILDING COMPANY</span></div>
    </div>

    <div class="phone">
      <svg width="60" height="60" viewBox="0 0 24 24" aria-hidden="true">
        <path fill="#6db33f" d="M6.6 10.8a15.1 15.1 0 0 0 6.6 6.6l2.2-2.2a1 1 0 0 1 1-.25 11.4 11.4 0 0 0 3.6.57 1 1 0 0 1 1 1V20a1 1 0 0 1-1 1A17 17 0 0 1 3 4a1 1 0 0 1 1-1h3.5a1 1 0 0 1 1 1c0 1.25.2 2.45.57 3.57a1 1 0 0 1-.25 1z"/>
        <path fill="none" stroke="#6db33f" stroke-width="1.6" stroke-linecap="round" d="M14 3.5a7 7 0 0 1 6.5 6.5M14 7a3.5 3.5 0 0 1 3 3"/>
      </svg>
      <span>472.555.0188</span>
    </div>

    <div class="contacts">
      <div class="contact">
        <span class="contact-line">
          <svg width="18" height="18" viewBox="0 0 20 20" aria-hidden="true"><g fill="none" stroke="#6db33f" stroke-width="1.6"><circle cx="10" cy="10" r="8"/><ellipse cx="10" cy="10" rx="3.5" ry="8"/><path d="M2 10h16M3.5 6h13M3.5 14h13"/></g></svg>
          thornwellbuildingcompany
        </span>
        <span class="contact-tail">.com</span>
      </div>
      <div class="contact">
        <span class="contact-line">
          <svg width="18" height="14" viewBox="0 0 20 14" aria-hidden="true"><rect x="1" y="1" width="18" height="12" fill="#6db33f"/><path d="M1 1l9 7 9-7" fill="none" stroke="#1c1c1c" stroke-width="1.5"/></svg>
          thornwellbuildingcompany
        </span>
        <span class="contact-tail">@mailvero.com</span>
      </div>
    </div>

    <p class="license">License No.: 4620385</p>
  </section>
</main>
</body>
</html>
```